Real Estate Open House A Frame Sign

The sign is 22" wide and 28" tall. This sign is used to post around the neighbourhood to direct people to an open house (home that is for sale). It is also used for self-promotion.

Designwise
- I just want something with a modern look, simple and clean.
- I want my picture and business logo on the left side.
- On the right side, website (www.lumwick-realestate.com) and my phone (555-374-9126), then a blank space where I can write an address when I need to.

I'm not sure how I want the overall design look. I'm very open-minded and I'm depending on your creative mind to come up with something.

If you have any questions, please let me know.

```html
<!DOCTYPE html>
<html lang="en">
<head>
<meta charset="utf-8">
<title>Lumwick Real Estate – Home For Sale Sign</title>
<link href="https://fonts.googleapis.com/css2?family=Montserrat:wght@400&family=Open+Sans:wght@400;700&display=swap" rel="stylesheet">
<style>
  :root {
    --brand-blue: #154580;
    --band-blue: #1c4d8a;
    --rule-grey: #cfd1d4;
    --paper: #ffffff;
    --ink-light: #ffffff;
    --portrait-light: #d9dde3;
    --portrait-dark: #2c3038;
  }
  * { margin: 0; padding: 0; box-sizing: border-box; }
  html, body {
    width: 992px;
    height: 1200px;
    overflow: hidden;
    background: var(--paper);
  }
  .sign {
    position: relative;
    width: 992px;
    height: 1200px;
    background: var(--paper);
    overflow: hidden;
    font-family: "Open Sans", Arial, sans-serif;
  }
  .sign-shapes {
    position: absolute;
    inset: 0;
    width: 992px;
    height: 1200px;
  }
  .brand {
    position: absolute;
    top: 44px;
    left: 0;
    width: 992px;
    text-align: center;
    color: var(--ink-light);
    font-family: "Montserrat", Arial, sans-serif;
    font-weight: 400;
  }
  .brand-name {
    display: block;
    font-size: 100px;
    line-height: 1.1;
    letter-spacing: 6px;
  }
  .brand-sub {
    display: block;
    margin-top: 14px;
    font-size: 34px;
    letter-spacing: 18px;
    padding-left: 18px;
  }
  .portrait {
    position: absolute;
    left: 0;
    top: 340px;
    width: 450px;
    height: 860px;
  }
  .headline {
    position: absolute;
    left: 478px;
    top: 318px;
    color: var(--brand-blue);
    font-weight: 700;
    line-height: 1;
  }
  .headline-main {
    display: block;
    font-size: 150px;
    letter-spacing: -1px;
  }
  .headline-sub {
    display: block;
    margin-top: 12px;
    font-size: 98px;
    letter-spacing: -1px;
  }
  .details {
    position: absolute;
    left: 482px;
    top: 712px;
    width: 480px;
    color: var(--ink-light);
  }
  .agent-name,
  .agent-role {
    display: block;
    font-size: 54px;
    line-height: 70px;
  }
  .contact-phone {
    display: flex;
    align-items: center;
    gap: 12px;
    margin-top: 14px;
    font-size: 42px;
    line-height: 56px;
  }
  .contact-phone svg { width: 40px; height: 40px; flex: none; }
  .contact-web {
    display: block;
    margin-top: 10px;
    font-size: 31px;
    line-height: 44px;
  }
  .contact-web strong { font-weight: 700; }
  .address-space {
    position: absolute;
    left: 482px;
    top: 1030px;
    width: 480px;
    height: 140px;
    background: var(--paper);
    border-radius: 6px;
  }
</style>
</head>
<body>
  <div class="sign">
    <svg class="sign-shapes" viewBox="0 0 992 1200" aria-hidden="true">
      <path d="M0 238 Q496 358 992 238" fill="none" stroke="var(--rule-grey)" stroke-width="7"/>
      <path d="M0 0 H992 V230 Q496 350 0 230 Z" fill="var(--brand-blue)"/>
      <path d="M0 612 Q600 592 992 682" fill="none" stroke="var(--rule-grey)" stroke-width="7"/>
      <path d="M0 621 Q600 601 992 691 V1200 H0 Z" fill="var(--band-blue)"/>
    </svg>

    <header class="brand">
      <span class="brand-name">LUMWICK</span>
      <span class="brand-sub">REAL ESTATE</span>
    </header>

    <svg class="portrait" viewBox="0 0 450 860" role="img" aria-label="Portrait photo of the broker in a dark suit with arms crossed">
      <defs>
        <linearGradient id="portraitTone" x1="0" y1="0" x2="0" y2="1">
          <stop offset="0" stop-color="var(--portrait-light)"/>
          <stop offset="0.45" stop-color="#8a8f98"/>
          <stop offset="1" stop-color="var(--portrait-dark)"/>
        </linearGradient>
      </defs>
      <path d="M0 420 C40 380 110 360 150 340 C120 300 110 240 110 160 C110 60 160 0 230 0 C300 0 350 60 350 160 C350 240 340 300 310 340 C360 370 420 420 440 500 C450 600 440 760 420 860 H0 Z" fill="url(#portraitTone)"/>
    </svg>

    <h1 class="headline">
      <span class="headline-main">HOME</span>
      <span class="headline-sub">FOR SALE</span>
    </h1>

    <div class="details">
      <span class="agent-name">Evan Marlow</span>
      <span class="agent-role">Broker</span>
      <div class="contact-phone">
        <svg viewBox="0 0 44 44" aria-hidden="true">
          <circle cx="22" cy="22" r="19" fill="none" stroke="#fff" stroke-width="3"/>
          <path d="M17 11 C14 12 12 15 13 20 C14 26 18 31 23 33 C27 34 30 32 31 30 L27 26 L24 28 C21 26 19 23 18 19 L21 17 Z" fill="none" stroke="#fff" stroke-width="2.5" stroke-linejoin="round"/>
        </svg>
        <span>555-374-9126</span>
      </div>
      <span class="contact-web">www.<strong>lumwick-realestate</strong>.com</span>
    </div>

    <div class="address-space" aria-label="Blank space for writing the open house address"></div>
  </div>
</body>
</html>
```